Halvern Capital, Inc.

We need a website design for a new company based in Orange County, CA but will be serving client's throughout all of California. We provide non-recourse loans/ pre-litigation funding for client's in personal injury and employment cases. Generally, if a client has an active case and they need money for cost of living, the client will contact a company like ours to provide a loan. We would like to see designs that are sleek, simple and easy to use. The final design should communicate trustworthiness, financial safety and promptness.

Hi, I like TK's designs. I am having him work on a hybrid of two of his designs. We had a little miscommunication, but we are almost there. Best, Ren

```html
<!DOCTYPE html>
<html lang="en">
<head>
<meta charset="utf-8">
<title>Halvern Capital, Inc.</title>
<link href="https://fonts.googleapis.com/css2?family=Cinzel:wght@400;600;700&family=PT+Sans:wght@400;700&family=Montserrat:wght@500;600;700&display=swap" rel="stylesheet">
<style>
:root{
  --gold:#c6a21c;
  --gold-dark:#a9880f;
  --black:#000;
  --ink:#111;
  --navy:#1b1443;
  --text:#555;
  --grey-panel:#ececec;
  --line:#d8d8d8;
  --white:#fff;
  --cream:#f7f2dc;
}
*{box-sizing:border-box;margin:0;padding:0}
html,body{width:1200px;height:2917px;overflow:hidden}
body{font-family:"PT Sans",Arial,sans-serif;color:var(--text);background:var(--white);position:relative}
.serif{font-family:"Cinzel",Georgia,serif}
.gold{color:var(--gold)}

/* top bar */
.topbar{height:43px;background:var(--gold);color:var(--white);display:flex;justify-content:flex-end;align-items:center;padding-right:78px;gap:26px;font-size:14px}
.topbar .item{display:flex;align-items:center;gap:8px}
.topbar .phone{font-weight:700;font-size:21px}

/* header */
.header{height:82px;display:flex;align-items:center;justify-content:space-between;padding:0 78px 0 80px}
.brand{font-family:"Cinzel",Georgia,serif;font-weight:700;font-size:30px;color:var(--ink);letter-spacing:.5px}
.nav{display:flex;align-items:center;gap:30px;font-family:"Montserrat",Arial,sans-serif;font-size:14px;font-weight:500;color:var(--ink)}
.nav .active{color:var(--gold);display:flex;align-items:center;gap:6px}

/* hero */
.hero{position:relative;height:552px;background:linear-gradient(100deg,#3f4a55 0%,#7f8c96 30%,#b9c4cc 55%,#dfe6ea 80%,#eef2f4 100%)}
.hero-arrow{position:absolute;top:118px;width:50px;height:50px;border-radius:50%;background:rgba(60,60,60,.45);display:flex;align-items:center;justify-content:center}
.hero-arrow.prev{left:12px}.hero-arrow.next{right:12px}
.hero-caption{position:absolute;left:0;right:0;bottom:0;height:62px;background:rgba(20,20,20,.55);color:var(--white);font-family:"Montserrat",Arial,sans-serif;font-weight:700;font-size:16px;letter-spacing:.4px;padding:20px 0 0 78px}
.consult{position:absolute;left:757px;top:95px;width:356px;height:416px;background:var(--black)}
.consult-head{height:82px;background:var(--gold);clip-path:polygon(0 0,100% 0,100% 70%,50% 100%,0 70%);text-align:center;color:var(--white);font-family:"Cinzel",Georgia,serif;font-weight:600;font-size:20px;padding-top:20px;letter-spacing:.5px}
.consult-form{padding:28px 30px 0 30px}
.field{height:37px;background:var(--cream);border-radius:3px;margin-bottom:12px;display:flex;align-items:center;gap:10px;padding:0 12px;font-size:12px;color:#333}
.field.msg{height:68px;align-items:flex-start;padding-top:12px}
.submit{display:block;margin:20px auto 0;width:124px;height:38px;background:var(--gold);color:var(--white);font-family:"Cinzel",Georgia,serif;font-weight:700;font-size:16px;text-align:center;line-height:38px;letter-spacing:.5px}

/* intro */
.intro{position:absolute;left:78px;top:677px;width:1044px;height:210px;background:var(--grey-panel);border-bottom:5px solid var(--gold);text-align:center;padding-top:46px;box-shadow:0 22px 20px -14px rgba(0,0,0,.3)}
.intro h1{font-family:"Cinzel",Georgia,serif;font-weight:600;font-size:40px;color:var(--ink)}
.intro p{font-size:14px;line-height:27px;width:860px;margin:20px auto 0}
.intro .notch{position:absolute;left:516px;bottom:-14px;width:0;height:0;border-left:8px solid transparent;border-right:8px solid transparent;border-top:9px solid var(--gold)}

/* services */
.section-title{position:absolute;left:0;width:1200px;text-align:center;font-family:"Cinzel",Georgia,serif;font-weight:600;font-size:46px;color:var(--ink)}
.section-sub{position:absolute;left:0;width:1200px;text-align:center;font-size:14px}
.service{position:absolute;top:1157px;width:477px;height:315px;background:var(--white);border:1px solid var(--line);box-shadow:6px 6px 0 var(--gold);text-align:center;padding-top:100px}
.service h3{font-family:"Cinzel",Georgia,serif;font-weight:700;font-size:22px;color:var(--ink)}
.service p{font-size:14px;line-height:27px;width:380px;margin:14px auto 0}
.service .icon{position:absolute;left:196px;top:-46px;width:92px;height:92px;background:var(--white);border:1px solid var(--ink);box-shadow:6px 6px 0 var(--gold);display:flex;align-items:center;justify-content:center}
.service .more{position:absolute;left:216px;bottom:-1px;width:50px;height:26px;border-radius:25px 25px 0 0;background:var(--black);color:var(--white);text-align:center;font-size:24px;line-height:30px}

/* about */
.about{position:absolute;left:0;top:1552px;width:1200px;height:416px;display:flex}
.about-text{width:600px;background:var(--gold);padding:60px 60px 0 78px;color:var(--white)}
.about-text h2{font-family:"Cinzel",Georgia,serif;font-weight:400;font-size:36px;line-height:40px;color:var(--ink)}
.about-text h2 strong{font-weight:600;font-size:40px}
.about-text p{font-size:14px;line-height:27px;margin-top:22px}
.btn-outline{display:inline-block;margin-top:24px;border:2px solid var(--white);padding:10px 16px;font-family:"Cinzel",Georgia,serif;font-weight:600;font-size:18px;color:var(--white)}
.about-photo{flex:1;background:linear-gradient(180deg,#8a8a86 0%,#a7a59f 40%,#6e6d69 100%)}

/* news */
.news-title{color:var(--navy)}
.news-card{position:absolute;top:2161px;width:312px;height:336px;background:var(--white);box-shadow:0 2px 8px rgba(0,0,0,.15);border-bottom:4px solid var(--gold);text-align:center}
.news-card .photo{height:208px}
.news-card .date{font-size:13px;color:var(--gold);margin-top:24px}
.news-card h4{font-family:"Cinzel",Georgia,serif;font-weight:700;font-size:16px;line-height:24px;color:var(--ink);margin-top:12px}

/* footer */
.footer{position:absolute;left:0;top:2563px;width:1200px;height:280px;background:var(--black);color:#bbb}
.footer h5{font-family:"Cinzel",Georgia,serif;font-weight:600;font-size:22px;color:var(--white);letter-spacing:.5px}
.links{position:absolute;left:78px;top:30px}
.links ul{list-style:none;margin-top:24px}
.links li{font-size:14px;line-height:33px;padding-left:18px;position:relative}
.links li::before{content:"";position:absolute;left:0;top:14px;width:6px;height:6px;border-radius:50%;background:var(--gold)}
.contact{position:absolute;left:364px;top:30px}
.contact .row{display:flex;gap:22px;font-size:14px;line-height:26px;margin-top:14px}
.contact .row svg{flex:none;margin-top:3px}
.contact .first{margin-top:22px}
.map{position:absolute;left:622px;top:34px;width:186px;height:186px;border-radius:50%;border:5px solid var(--gold);background:radial-gradient(circle at 50% 50%,#f1ede2,#dcd8c9)}
.footer-about{position:absolute;left:877px;top:30px;width:260px}
.footer-about p{font-size:14px;line-height:27px;margin-top:20px}
.bottombar{position:absolute;left:0;top:2843px;width:1200px;height:74px;background:var(--gold);color:var(--white);font-size:13px;padding:0 78px;display:flex;align-items:center;justify-content:space-between}
.social{display:flex;gap:14px}
.social span{width:46px;height:46px;border-radius:50%;background:var(--white)}
</style>
</head>
<body>

<div class="topbar">
  <div class="item">Call For Free Consultation :
    <svg width="24" height="24" viewBox="0 0 24 24"><circle cx="12" cy="12" r="12" fill="#fff"/><path d="M8 6.5l2 2-1.2 1.6c.7 1.6 2 2.9 3.6 3.6l1.6-1.2 2 2-1.4 1.6c-3.8-.6-6.8-3.6-7.4-7.4z" fill="#c6a21c"/></svg>
    <span class="phone">123 456 7890</span></div>
  <div class="item">
    <svg width="18" height="13" viewBox="0 0 18 13"><rect width="18" height="13" rx="1.5" fill="#fff"/><path d="M1 1l8 6 8-6" stroke="#c6a21c" stroke-width="1.5" fill="none"/></svg>
    info@halverncapital.com</div>
</div>

<header class="header">
  <div class="brand">Halvern Capital, <span class="gold">Inc.</span></div>
  <nav class="nav">
    <span class="active">HOME <svg width="10" height="6"><path d="M0 0h10L5 6z" fill="#c6a21c"/></svg></span>
    <span>ABOUT</span><span>SERVICES</span><span>NEWS</span><span>CONTACT</span>
    <svg width="16" height="16" viewBox="0 0 16 16"><circle cx="6.5" cy="6.5" r="5" stroke="#111" stroke-width="2" fill="none"/><path d="M10.5 10.5l4 4" stroke="#111" stroke-width="2.4"/></svg>
  </nav>
</header>

<section class="hero" role="img" aria-label="Two advisers reviewing a tablet together in a bright office">
  <div class="hero-arrow prev"><svg width="12" height="20"><path d="M10 2L2 10l8 8" stroke="#fff" stroke-width="2" fill="none"/></svg></div>
  <div class="hero-arrow next"><svg width="12" height="20"><path d="M2 2l8 8-8 8" stroke="#fff" stroke-width="2" fill="none"/></svg></div>
  <div class="hero-caption">HALVERN CAPITAL LITIGATION FUNDING SPECIALISTS WHO CARE ABOUT YOUR CASE</div>
  <div class="consult">
    <div class="consult-head">GET FREE CONSULTATION</div>
    <div class="consult-form">
      <div class="field"><svg width="14" height="14" viewBox="0 0 14 14"><circle cx="7" cy="4" r="3" fill="#333"/><path d="M1 14c0-4 3-6 6-6s6 2 6 6z" fill="#333"/></svg>Name</div>
      <div class="field"><svg width="14" height="14" viewBox="0 0 14 14"><path d="M3 1l2.5 2.5-1.4 1.8c.8 1.8 2 3 3.8 3.8l1.8-1.4L12.2 10l-1.6 2C5.8 11.6 2.4 8.2 2 3.4z" fill="none" stroke="#333" stroke-width="1.3"/></svg>Contact No</div>
      <div class="field"><svg width="15" height="11" viewBox="0 0 15 11"><rect x=".6" y=".6" width="13.8" height="9.8" fill="none" stroke="#333" stroke-width="1.2"/><path d="M1 1l6.5 5L14 1" stroke="#333" stroke-width="1.2" fill="none"/></svg>Email</div>
      <div class="field msg"><svg width="14" height="14" viewBox="0 0 14 14"><rect x=".6" y="2" width="10" height="11" fill="none" stroke="#333" stroke-width="1.2"/><path d="M5 9l1-3 6-5 2 2-6 5z" fill="#333"/></svg>Message...</div>
      <div class="submit">SUBMIT</div>
    </div>
  </div>
</section>

<div class="intro">
  <h1>Halvern Capital, <span class="gold">Inc.</span></h1>
  <p>Lorem Ipsum is simply dummy text of the printing and typesetting industry. Lorem Ipsum has been the industry's standard dummy text ever since the 1500s, when an unknown printer took a galley</p>
  <span class="notch"></span>
</div>

<h2 class="section-title" style="top:966px">Services We <span class="gold">Provided</span></h2>
<p class="section-sub" style="top:1030px">Lorem Ipsum is simply dummy text of the printing and typesetting industry Lorem Ipsum has been th</p>

<div class="service" style="left:78px">
  <div class="icon"><svg width="56" height="56" viewBox="0 0 56 56"><rect x="6" y="4" width="30" height="40" fill="#fff" stroke="#111" stroke-width="3"/><rect x="12" y="10" width="30" height="40" fill="#111"/><text x="27" y="36" font-family="PT Sans" font-weight="700" font-size="20" fill="#fff" text-anchor="middle">$</text><circle cx="44" cy="40" r="7" fill="#fff" stroke="#111" stroke-width="3"/><rect x="38" y="46" width="12" height="6" fill="#111"/></svg></div>
  <h3>Non-Recourse Loans</h3>
  <p>Lorem Ipsum is simply dummy text of the printing and typesetting industry. Lorem Ipsum has been the industry's standard dummy text ever since thes, when an unknown printer took a galley of type and</p>
  <div class="more">+</div>
</div>

<div class="service" style="left:638px">
  <div class="icon"><svg width="56" height="56" viewBox="0 0 56 56"><circle cx="28" cy="16" r="12" fill="#111"/><text x="28" y="23" font-family="PT Sans" font-weight="700" font-size="18" fill="#fff" text-anchor="middle">$</text><path d="M4 36h10l8 4h12c3 0 3 4 0 4H24h12l12-8c3-2 6 1 4 3L38 50H14l-10-4z" fill="#111"/></svg></div>
  <h3>Pre-Litigation Funding</h3>
  <p>Lorem Ipsum is simply dummy text of the printing and typesetting industry. Lorem Ipsum has been the industry's standard dummy text ever since thes, when an unknown printer took a galley of type and</p>
  <div class="more">+</div>
</div>

<section class="about">
  <div class="about-text">
    <h2>About<br><strong>Halvern Capital, Inc.</strong></h2>
    <p>Lorem Ipsum is simply dummy text of the printing and typesetting industry. Lorem Ipsum has been the industry's standard dummy text ever since the 1500s, when an unknown printer took a galley of type and scrambled it to make a type specimen book Lorem Ipsum is simply dummy text of the printing and typesetting industry.</p>
    <span class="btn-outline">LEARN MORE</span>
  </div>
  <div class="about-photo" role="img" aria-label="Three professionals in suits walking past courthouse columns"></div>
</section>

<h2 class="section-title news-title" style="top:2026px">Latest News</h2>
<p class="section-sub" style="top:2080px;width:900px;left:150px;line-height:27px">Lorem Ipsum is simply dummy text of the printing and typesetting industry. Lorem Ipsum has been the industry's standard dummy text ever since the 1500s, when an unknown printer took a galley</p>

<article class="news-card" style="left:109px">
  <div class="photo" role="img" aria-label="Hands with a bandaged wrist typing on a laptop" style="background:linear-gradient(135deg,#4a3526,#8b6a4d 50%,#d9d4cc)"></div>
  <div class="date">03 january 2018</div>
  <h4>Lorem Ipsum is simply print<br>of the printing.</h4>
</article>
<article class="news-card" style="left:444px">
  <div class="photo" role="img" aria-label="Colleagues meeting in an office" style="background:linear-gradient(135deg,#2e3f48,#6f8893 50%,#c7cfd2)"></div>
  <div class="date">03 january 2018</div>
  <h4>Lorem Ipsum is simply print<br>of the printing.</h4>
</article>
<article class="news-card" style="left:778px">
  <div class="photo" role="img" aria-label="Person with a leg cast and crutch resting on a bench" style="background:linear-gradient(135deg,#3a3a38,#777670 50%,#bcbab4)"></div>
  <div class="date">03 january 2018</div>
  <h4>Lorem Ipsum is simply print<br>of the printing.</h4>
</article>

<footer class="footer">
  <div class="links">
    <h5>Useful Links</h5>
    <ul><li>Home</li><li>About Us</li><li>Services</li><li>News</li><li>Contact Us</li></ul>
  </div>
  <div class="contact">
    <h5>Contact US</h5>
    <div class="row first"><svg width="20" height="26" viewBox="0 0 20 26"><path d="M10 0a10 10 0 0110 10c0 7-10 16-10 16S0 17 0 10A10 10 0 0110 0z" fill="#c6a21c"/><circle cx="10" cy="10" r="4" fill="#000"/></svg><span>101 - Loremipsum simple text<br>of print and type text.</span></div>
    <div class="row"><svg width="20" height="20" viewBox="0 0 20 20"><path d="M4 1l4 4-2 2.5c1.2 2.8 3.6 5.2 6.5 6.5L15 12l4 4-2.5 3C8.5 18 2 11.5 1 3.5z" fill="#c6a21c"/></svg><span>123 456 7890</span></div>
    <div class="row"><svg width="20" height="20" viewBox="0 0 20 20"><rect x="1" y="5" width="18" height="14" fill="#c6a21c"/><rect x="5" y="1" width="10" height="6" fill="none" stroke="#c6a21c" stroke-width="2"/><rect x="5" y="9" width="10" height="2" fill="#000"/><rect x="5" y="13" width="10" height="2" fill="#000"/></svg><span>123 456 7890</span></div>
    <div class="row"><svg width="20" height="15" viewBox="0 0 20 15"><rect width="20" height="15" fill="#c6a21c"/><path d="M1 1l9 7 9-7" stroke="#000" stroke-width="1.6" fill="none"/></svg><span>info@halverncapital.com</span></div>
  </div>
  <div class="map" role="img" aria-label="Street map showing the office location"></div>
  <div class="footer-about">
    <h5>Halvern Capital, <span class="gold">Inc.</span></h5>
    <p>Lorem Ipsum is simply dummy text of the printing and typesetting industry. Lorem Ipsum has been the industry's standard dummy text ever since the 1500s, when an unknown.</p>
  </div>
</footer>

<div class="bottombar">
  <span>©Halvern Capital, Inc. -2019 All Right Reserved.</span>
  <div class="social" aria-label="Social links"><span></span><span></span><span></span></div>
</div>

</body>
</html>
```